Business card design for new eCommerce site focusing on integrity and strong businsess tactics

We need a business card that will stand out and be memorable. Something with color that matches our company logo colors. Think high end version of Tallyhop. There are 2 logos provided. The parent company is called Brightwell Craft Partners and we are presenting a new and very exciting eCommerce site called KestrelTradeHub.example.

Target Market(s)

Our target markets are in the Activities, Food and Beverage, Health and Beauty

Industry/Entity Type

Marketing

Contact Information for Business Card

We have 4 members that need cards...I will provide all info to the winner of the design contest
Business Address is
47390 West 63rd Lane, Suite K204
Phoenix AZ 85061

Font styles to use
Serif
Sans Serif

Colors

Designer to choose colors to be used in the design.

Requirements
Must have
• The card must be memorable...should be unique in design but must exude integrity and be playful .
• I have provided several colors or our parent company...please feel free to use which ever
Nice to have
• I will leave this up to you. Feel free to use other images of your choosing that wraps around our client.....Activities, Dining, Health, Beauty
Should not have
• just dont be boring

```html
<!DOCTYPE html>
<html lang="en">
<head>
<meta charset="utf-8">
<title>KestrelTradeHub.example Business Card</title>
<link href="https://fonts.googleapis.com/css2?family=Jost:wght@400;500;600&display=swap" rel="stylesheet">
<style>
  :root {
    --backdrop: #2a2a2a;
    --blue-light: #41b9d6;
    --blue: #2e82b6;
    --blue-deep: #2a73a8;
    --green: #8cc63f;
    --green-light: #b6de4d;
    --green-deep: #76bd31;
    --paper: #f4f4f4;
    --ink-grey: #555a60;
    --white: #ffffff;
  }
  * { box-sizing: border-box; margin: 0; padding: 0; }
  html, body { width: 1200px; height: 960px; overflow: hidden; }
  body {
    background: var(--backdrop);
    font-family: "Jost", sans-serif;
    position: relative;
  }
  .card {
    position: absolute;
    width: 600px;
    height: 342px;
    border-radius: 20px;
    overflow: hidden;
  }
  .card-front { left: 302px; top: 131px; background: var(--paper); }
  .card-back {
    left: 299px; top: 490px;
    background: linear-gradient(120deg, var(--green-light) 0%, var(--green-deep) 45%, var(--green-deep) 100%);
    color: var(--white);
    text-align: center;
  }
  .front-panel { position: absolute; inset: 0; }
  .contact-block { position: absolute; left: 28px; top: 72px; color: var(--white); }
  .person-name { font-size: 23px; font-weight: 500; color: var(--green); letter-spacing: 0.2px; line-height: 1; }
  .person-title { font-size: 14.5px; margin-top: 5px; letter-spacing: 0.2px; }
  .address { font-size: 14.5px; line-height: 17.5px; margin-top: 12px; }
  .contact-list { list-style: none; margin-top: 12px; font-size: 14.5px; line-height: 19.5px; }
  .contact-list li { display: flex; align-items: center; gap: 8px; }
  .contact-list svg { width: 13px; height: 13px; flex: none; }
  .front-brand { position: absolute; left: 310px; top: 149px; width: 270px; text-align: center; }
  .brand-name-front { font-size: 20px; font-weight: 500; color: var(--blue); letter-spacing: -0.3px; white-space: nowrap; }
  .tagline-front { font-size: 12px; color: var(--ink-grey); letter-spacing: 1.3px; margin-top: 1px; white-space: nowrap; }
  .brand-name-back { position: absolute; left: 0; right: 0; top: 132px; font-size: 35px; font-weight: 500; letter-spacing: -0.6px; }
  .tagline-back { position: absolute; left: 0; right: 0; top: 182px; font-size: 17px; letter-spacing: 2.6px; }
  .slogan {
    position: absolute; left: 120px; right: 120px; top: 279px;
    display: flex; align-items: center; gap: 6px;
    font-size: 14px; font-weight: 600; letter-spacing: 1px; white-space: nowrap;
  }
  .slogan::before, .slogan::after {
    content: ""; flex: 1; height: 1px;
    background: linear-gradient(90deg, rgba(255,255,255,0), var(--white));
  }
  .slogan::after { background: linear-gradient(90deg, var(--white), rgba(255,255,255,0)); }
</style>
</head>
<body>
  <section class="card card-front">
    <svg class="front-panel" viewBox="0 0 600 342" width="600" height="342" role="img" aria-label="Decorative wave band in blue, white and green">
      <defs>
        <linearGradient id="panelBlue" x1="0" y1="0" x2="1" y2="1">
          <stop offset="0" stop-color="var(--blue-light)"/>
          <stop offset="0.45" stop-color="var(--blue)"/>
          <stop offset="1" stop-color="var(--blue-deep)"/>
        </linearGradient>
      </defs>
      <path class="panel" d="M0,0 H285 C255,110 255,230 300,342 H0 Z" fill="url(#panelBlue)"/>
    </svg>

    <div class="contact-block">
      <h1 class="person-name">EVAN MARLOW</h1>
      <p class="person-title">CEO/FOUNDER</p>
      <p class="address">47390 West 63rd Lane<br>Suite K204<br>Phoenix AZ 85061</p>
      <ul class="contact-list">
        <li><svg viewBox="0 0 16 16"><path d="M3 1.5l3 .5 1 3.5-2 1.5c1 2 2.5 3.5 4.5 4.5l1.5-2 3.5 1 .5 3c-6 1-13-6-12-12z" fill="var(--green)"/></svg>555 214 0387</li>
        <li><svg viewBox="0 0 16 16"><rect x="4" y="1" width="8" height="14" rx="1.5" fill="none" stroke="var(--green)" stroke-width="1.8"/><rect x="7" y="12" width="2" height="1.2" fill="var(--green)"/></svg>555 730 6192</li>
        <li><svg viewBox="0 0 16 16"><rect x="1" y="3.5" width="14" height="9" fill="var(--green)"/><path d="M1.5 4l6.5 5 6.5-5" fill="none" stroke="var(--blue)" stroke-width="1.2"/></svg>evan@kestreltradehub.example</li>
        <li><svg viewBox="0 0 16 16"><circle cx="8" cy="8" r="6.5" fill="var(--green)"/><path d="M1.5 8h13M8 1.5c-3 3.5-3 9.5 0 13M8 1.5c3 3.5 3 9.5 0 13" fill="none" stroke="var(--blue)" stroke-width="0.9"/></svg>www.kestreltradehub.example</li>
      </ul>
    </div>

    <div class="front-brand">
      <p class="brand-name-front">KestrelTradeHub.example</p>
      <p class="tagline-front">Activities-Dining-Health-Beauty</p>
    </div>
  </section>

  <section class="card card-back">
    <p class="brand-name-back">KestrelTradeHub.example</p>
    <p class="tagline-back">Activities-Dining-Health-Beauty</p>
    <p class="slogan">LOOKING OUT FOR YOU</p>
  </section>
</body>
</html>
```